Delivery Docket urgent plus require many other designs for more stationary after this.

We need a new delivery docket design urgently as the one we have needs updating and we have changed our company name. Please do not copy the one I have uploaded as we do not feel this looks professional enough. I uploaded it as a few designers requested to see what we are currently using thank you.
It is quite complex in that we need a range of information to be on the one docket.
We are a Transport Company based in Australia that has a wide variety of items that we deliver such as water, sand and gravels and heavy equipment transport.
We would prefer to keep this design to A5 size as we will get them made into books. We are looking for a modern professional look. Although it is only a delivery docket this is given to all our customers so needs to look impressive.

We need our new logo on the docket (RWT). There will also need to be areas for our address and contact numbers, email etc these will be supplied to the winning designer to make the final adjustments so for now just put something generic in these spaces.
Needs to have an area for customer details, purchase order number, date and docket number (docket number to be in red)
Needs a section where we can list the type of product / and or service that has been provided and the amount / qty usually 3 lines will be enough for this. Need area under this where the customer can sign name and print name to say that the goods / and or services have been received.

Also required somewhere on the docket are the words, Tax Invoice will be issued based on the information provided on this docket. Conditions on back of page

We then need a separate section on the same page which we will use internally that the staff member can tear off and hand into the office. On this section it needs to have area where the driver can list km at start of job and at end with space to calculate km travelled, details of fuel purchased eg amount and litres, vehicle that is being used. also need to log down wheel bearing temps.
prime mover needs spaces as follows
Steer axel FL____________ Steer axel FR _________ 1st drive axel L_______
1st drive axel R_________ 2nd drive axel L_______ 2nd drive axel R________

For the trailers need something similar x 2 as have 2 trailers
1st axel DS_________ 1st axel PS_________ 2nd axel DS__________
2nd axel PS_________ 3rd axel DS_________ 3rd axel PS__________

I have included a few examples of designs we have used in past and ones that we like so you can get an idea of the colours we prefer, I have included some of the designs we are currently receiving for our logo that I like so you can get idea again of colours we prefer. There is much more we need designed also such as time sheets, more delivery dockets and letter heads so there is a lot of more work available to the winning designer.

Thank you

Target Market(s)

Customers

Font styles to use
Serif
Sans Serif

Colors

Designer to choose colors to be used in the design.

Requirements
Should not have
• Please don't copy old docket as we do not like it and nned new info on new design thank you

```html
<!DOCTYPE html>
<html lang="en">
<head>
<meta charset="utf-8">
<title>RWT Delivery Docket – Front and Back</title>
<link href="https://fonts.googleapis.com/css2?family=Open+Sans:wght@400;600;700&display=swap" rel="stylesheet">
<style>
  :root{
    --stage-top:#2b2b2b;
    --stage-bottom:#0d0d0d;
    --ink:#000;
    --paper:#fff;
    --label:#fff;
    --docket-red:#e0141b;
    --steel:#c9c9c9;
    --steel-dark:#6e6e6e;
    --line:#000;
  }
  html,body{margin:0;padding:0;overflow:hidden}
  body{
    width:1200px;height:1200px;
    background:radial-gradient(ellipse at 50% 40%,var(--stage-top),var(--stage-bottom) 80%);
    font-family:"Open Sans",Arial,sans-serif;
    position:relative;
  }
  .side-label{
    position:absolute;top:125px;width:546px;text-align:center;
    color:var(--label);font-size:45px;font-weight:400;margin:0;line-height:1;
  }
  .side-label--front{left:34px}
  .side-label--back{left:617px}
  .panel{position:absolute;top:201px;width:546px;height:843px;display:block}
  .panel--front{left:34px}
  .panel--back{left:617px;background:var(--paper)}
  .form-label{font-size:10px;fill:var(--ink)}
  .bar-label{font-size:12px;fill:#fff}
  .row-text{font-size:12.5px;fill:var(--ink)}
  .contact{font-size:14px;fill:var(--ink)}
  .cell{fill:none;stroke:var(--line);stroke-width:1.2}
</style>
</head>
<body>
  <h2 class="side-label side-label--front">Front</h2>
  <h2 class="side-label side-label--back">Back</h2>

  <!-- Front cover -->
  <svg class="panel panel--front" viewBox="0 0 682 1054" xmlns="http://www.w3.org/2000/svg">
    <defs>
      <linearGradient id="sketchTone" x1="0" y1="0" x2="0" y2="1">
        <stop offset="0" stop-color="#d8d8d8"/>
        <stop offset=".5" stop-color="#8a8a8a"/>
        <stop offset="1" stop-color="#5a5a5a"/>
      </linearGradient>
      <linearGradient id="outbackTone" x1="0" y1="0" x2="0" y2="1">
        <stop offset="0" stop-color="#8d98a4"/>
        <stop offset=".35" stop-color="#aeb2b4"/>
        <stop offset=".55" stop-color="#3a3a38"/>
        <stop offset=".8" stop-color="#8a5a3e"/>
        <stop offset="1" stop-color="#a36d4c"/>
      </linearGradient>
      <radialGradient id="meshTone" cx=".5" cy=".5" r=".6">
        <stop offset="0" stop-color="#4a4a4a"/>
        <stop offset="1" stop-color="#0a0a0a"/>
      </radialGradient>
    </defs>
    <rect class="cover-photo" x="0" y="610" width="682" height="444" fill="url(#outbackTone)" role="img" aria-label="Photo of a road train truck on a red dirt outback road"/>
    <rect class="cover-illustration" x="0" y="0" width="682" height="640" fill="url(#sketchTone)" role="img" aria-label="Sketched illustration of two prime mover trucks"/>
    <polygon class="chevron-band" points="0,560 340,190 682,560 682,650 340,300 0,650" fill="#1a1a1a" opacity=".92"/>
    <polygon class="chevron-edge" points="0,650 340,300 682,650 682,662 340,312 0,662" fill="var(--steel)"/>
    <polygon class="apex" points="340,249 427,319 253,319" fill="var(--steel-dark)"/>
    <polygon class="shade shade--left" points="145,600 320,775 175,920 0,745" fill="#777" opacity=".55"/>
    <polygon class="shade shade--right" points="537,600 682,745 507,920 362,775" fill="#777" opacity=".55"/>
    <polygon class="shade shade--base" points="340,640 520,820 340,810 160,820" fill="#555" opacity=".5"/>
    <polygon class="badge-frame" points="340,332 548,539 340,746 132,539" fill="var(--steel)"/>
    <polygon class="badge-core" points="340,348 532,539 340,730 148,539" fill="url(#meshTone)"/>
    <text x="340" y="580" text-anchor="middle" font-size="108" font-weight="700" fill="var(--steel)" font-family="'Open Sans',Arial,sans-serif">RWT</text>
  </svg>

  <!-- Docket back -->
  <svg class="panel panel--back" viewBox="0 0 682 1054" xmlns="http://www.w3.org/2000/svg">
    <defs>
      <radialGradient id="logoTile" cx=".5" cy=".5" r=".7">
        <stop offset="0" stop-color="#4a4a4a"/>
        <stop offset="1" stop-color="#050505"/>
      </radialGradient>
    </defs>
    <!-- brand tile -->
    <rect x="41" y="19" width="188" height="139" fill="url(#logoTile)"/>
    <text x="135" y="105" text-anchor="middle" font-size="50" font-weight="700" fill="var(--steel)">RWT</text>

    <!-- contact block -->
    <g class="contact-icons" fill="none" stroke="var(--ink)" stroke-width="1.3">
      <circle cx="507" cy="74" r="7.5"/><path d="M507 70a3 3 0 1 1 0 .1M507 78l-2.5-4h5z"/>
      <circle cx="507" cy="99" r="7.5"/><path d="M503 95c1 5 3 7 8 8l1-2-2-1-1 1c-2-1-3-2-4-4l1-1-1-2z"/>
      <circle cx="507" cy="124" r="7.5"/><rect x="503" y="121" width="8" height="6"/><path d="M503 121l4 3 4-3"/>
      <circle cx="507" cy="149" r="7.5"/><ellipse cx="507" cy="149" rx="3.5" ry="7.5"/><path d="M499.5 149h15M501 145h12M501 153h12"/>
    </g>
    <text class="contact" x="524" y="79">Address:</text>
    <text class="contact" x="524" y="104">123 456 7890</text>
    <text class="contact" x="524" y="129">info@rwt.com</text>
    <text class="contact" x="524" y="154">www.rwt.com</text>

    <!-- customer details -->
    <rect class="cell" x="41" y="176" width="598" height="138" stroke-width="2"/>
    <rect x="47" y="182" width="289" height="20" fill="var(--ink)"/>
    <text class="bar-label" x="191" y="196" text-anchor="middle">Customer Details</text>
    <rect class="cell" x="358" y="181" width="272" height="22"/>
    <text class="form-label" x="370" y="195">Delivery Docket:</text>
    <text x="573" y="199" text-anchor="middle" font-size="20" fill="var(--docket-red)">2050</text>
    <rect class="cell" x="47" y="208" width="289" height="21"/><text class="form-label" x="59" y="222">Name:</text>
    <rect class="cell" x="358" y="208" width="272" height="21"/><text class="form-label" x="370" y="222">Date:</text>
    <rect class="cell" x="47" y="235" width="289" height="21"/><text class="form-label" x="59" y="249">Purchase Order Number:</text>
    <rect class="cell" x="358" y="235" width="272" height="21"/>
    <rect class="cell" x="47" y="262" width="289" height="21"/><text class="form-label" x="59" y="276">Contact:</text>
    <rect class="cell" x="358" y="262" width="272" height="21"/><text class="form-label" x="370" y="276">Phone:</text>
    <rect class="cell" x="47" y="288" width="583" height="21"/><text class="form-label" x="59" y="302">Billing Address:</text>

    <!-- items table -->
    <rect x="41" y="335" width="598" height="31" fill="var(--ink)"/>
    <text class="bar-label" x="94" y="355" text-anchor="middle">Qty</text>
    <text class="bar-label" x="317" y="355" text-anchor="middle">Description</text>
    <text class="bar-label" x="563" y="355" text-anchor="middle">Price</text>
    <rect class="cell" x="41" y="335" width="598" height="291" stroke-width="2"/>
    <g stroke="var(--line)" stroke-width="1.6">
      <line x1="147" y1="335" x2="147" y2="626" stroke="#fff" stroke-width="0"/>
      <line x1="147" y1="335" x2="147" y2="626"/>
      <line x1="487" y1="335" x2="487" y2="626"/>
      <line x1="41" y1="397" x2="639" y2="397"/>
      <line x1="41" y1="427" x2="639" y2="427"/>
      <line x1="41" y1="458" x2="639" y2="458"/>
      <line x1="41" y1="488" x2="639" y2="488"/>
      <line x1="41" y1="519" x2="639" y2="519"/>
      <line x1="41" y1="550" x2="639" y2="550"/>
      <line x1="41" y1="581" x2="639" y2="581"/>
    </g>
    <text font-size="11" x="317" y="598" text-anchor="middle">This Invoice will be based on information provided on this docket.</text>
    <text font-size="11" x="317" y="615" text-anchor="middle">Conditions on back of page.</text>

    <!-- tear line -->
    <line x1="12" y1="646" x2="669" y2="646" stroke="var(--line)" stroke-width="1.5" stroke-dasharray="8 6"/>

    <!-- receipt signature -->
    <rect x="41" y="664" width="599" height="33" fill="var(--ink)"/>
    <rect class="cell" x="41" y="664" width="599" height="106" stroke-width="2"/>
    <line x1="341" y1="664" x2="341" y2="770" stroke="var(--line)" stroke-width="1.6"/>
    <line x1="341" y1="664" x2="341" y2="697" stroke="#fff" stroke-width="2"/>
    <text x="56" y="685" font-size="13" fill="#fff">Good Received by (Print Name)</text>
    <text x="360" y="685" font-size="13" fill="#fff">Signed:</text>

    <!-- job log -->
    <rect class="cell" x="41" y="783" width="598" height="48" stroke-width="1.8"/>
    <g stroke="var(--line)" stroke-width="1.4">
      <line x1="41" y1="807" x2="639" y2="807"/>
      <line x1="230" y1="783" x2="230" y2="831"/>
      <line x1="474" y1="783" x2="474" y2="831"/>
    </g>
    <text class="form-label" font-size="9.5" x="51" y="799">Start of Job:</text>
    <text class="form-label" font-size="9.5" x="237" y="799">End of Job:</text>
    <text class="form-label" font-size="9.5" x="483" y="799">Total KM Traveled:</text>
    <text class="form-label" font-size="9.5" x="51" y="823">Fuel Amount:</text>
    <text class="form-label" font-size="9.5" x="237" y="823">Vehical:</text>
    <text class="form-label" font-size="9.5" x="483" y="823">Wheel Temps:</text>

    <!-- wheel bearing temps -->
    <rect class="cell" x="67" y="843" width="548" height="199" stroke-width="1.8"/>
    <line x1="67" y1="942" x2="615" y2="942" stroke="var(--line)" stroke-width="1.6"/>
    <rect x="221" y="850" width="240" height="18" fill="var(--ink)"/>
    <text class="bar-label" x="341" y="864" text-anchor="middle">Prime Mover</text>
    <text class="row-text" x="341" y="901" text-anchor="middle">Steer axel FL____________ Steer axel FR _________ 1st drive axel L_______</text>
    <text class="row-text" x="341" y="931" text-anchor="middle">1st drive axel R_________ 2nd drive axel L_______ 2nd drive axel R________</text>
    <rect x="221" y="950" width="240" height="18" fill="var(--ink)"/>
    <text class="bar-label" x="341" y="964" text-anchor="middle">For the trailers</text>
    <text class="row-text" x="341" y="1002" text-anchor="middle">1st axel DS_________ 1st axel PS_________ 2nd axel DS__________</text>
    <text class="row-text" x="341" y="1032" text-anchor="middle">2nd axel PS_________ 3rd axel DS_________ 3rd axel PS__________</text>
  </svg>
</body>
</html>
```